Granite Ridge College-Pinecrest Welcome Week

I am the Student Activities Coordinator at Granite Ridge College-Pinecrest. For Welcome Week 2013, I need a standard poster 24x36 with the list of events happening. Our theme is based on the popular Friday Late Laughs video "We Got a Kite"
http://www.vidtrove.example/clip/Q4mZp8sLwTe
Our theme is:
We're at the 'Crest!
Welcome Week 2013
Graphics on the poster should reflect popular images/designs of FLL We Got a Kite. However, the boat should be a steamboat instead of the yacht image.
Unfortunately, I have a lot of text to fit on the poster. Traditionally we go with 3 margins listing events. I'm attaching the word document of events and our logo to this proposal. I'll also attach a few google images of "We Got a Kite" that align with the type of theme I'm looking for.
One last thing, our logo contains mountains listing all of the different campuses. Remove the campus names and mountains all together. Use simply the Colorado flag C and "Granite Ridge College".
Thanks for considering this brief!
Glen
Target Market(s)
Our college students love to ski and snowboard. In fact, one of our degrees is "Alpine Slope Commerce". Their ages are 18-22.
Industry/Entity Type
Events
Look and feel

```html
<!DOCTYPE html>
<html lang="en">
<head>
<meta charset="utf-8">
<title>Welcome Week 2013 – Granite Ridge College-Pinecrest</title>
<link href="https://fonts.googleapis.com/css2?family=Anton&family=Raleway:wght@100&family=PT+Sans&display=swap" rel="stylesheet">
<style>
  :root {
    --bg: #131313;
    --panel: #28292b;
    --text: #f2f2f2;
    --hero-dark: #1d2226;
    --hero-mid: #56606a;
    --hero-light: #a9b1b6;
    --letter-light: #d4d5d6;
    --letter-dark: #9fa1a3;
    --ship-shadow: #232323;
    --logo-blue: #22306a;
    --logo-white: #ffffff;
  }
  html, body { margin: 0; padding: 0; overflow: hidden; }
  body { width: 804px; height: 1200px; background: var(--bg); }
  .poster {
    position: relative; width: 804px; height: 1200px; overflow: hidden;
    background: var(--bg); color: var(--text);
    font-family: "PT Sans", Arial, sans-serif;
  }
  .hero-photo {
    position: absolute; left: 0; top: 0; width: 804px; height: 470px;
    background:
      radial-gradient(ellipse at 50% 35%, var(--hero-mid) 0%, transparent 60%),
      linear-gradient(180deg, var(--hero-dark) 0%, var(--hero-mid) 55%, var(--hero-light) 80%, var(--hero-dark) 100%);
  }
  .hero-fade {
    position: absolute; left: 0; top: 400px; width: 804px; height: 80px;
    background: linear-gradient(180deg, transparent, var(--bg));
  }
  .headline { position: absolute; left: 0; top: 0; width: 804px; height: 470px; }
  .headline-kicker { font-family: "Raleway", sans-serif; font-weight: 100; fill: var(--text); }
  .headline-word { font-family: "Anton", Impact, sans-serif; }
  .event-title {
    position: absolute; top: 500px; left: 0; width: 804px; margin: 0;
    text-align: center; font-weight: 400; font-size: 29px; letter-spacing: 0.5px;
  }
  .footer-ship {
    position: absolute; left: 60px; top: 1010px; width: 560px; height: 170px; z-index: 0;
    background: radial-gradient(ellipse at 45% 65%, var(--ship-shadow) 0%, #1b1b1b 45%, transparent 72%);
  }
  .schedule {
    position: absolute; top: 564px; left: 109px; width: 587px; height: 480px; z-index: 1;
    display: flex; justify-content: space-between;
  }
  .schedule-column {
    width: 173px; height: 480px; background: var(--panel); padding: 10px 3px 0;
    box-sizing: border-box; text-align: center; font-size: 9px; line-height: 10.4px;
  }
  .event { margin: 0 0 10.4px; }
  .event p { margin: 0; white-space: nowrap; }
  .brand {
    position: absolute; left: 314px; top: 1094px; width: 184px; height: 96px; z-index: 1;
    background: var(--logo-blue); display: flex; align-items: center; gap: 8px;
    padding: 0 10px; box-sizing: border-box;
  }
  .brand-dot { width: 26px; height: 26px; border-radius: 50%; background: var(--logo-white); flex: none; }
  .brand-name {
    color: var(--logo-white); font-family: "PT Sans", Arial, sans-serif;
    font-size: 19px; line-height: 20px; text-transform: uppercase; letter-spacing: 0.3px;
  }
</style>
</head>
<body>
<div class="poster">
  <div class="hero-photo" role="img" aria-label="Photo of three men in tuxedos and sunglasses posing on the deck of a steamboat"></div>
  <div class="hero-fade"></div>

  <svg class="headline" viewBox="0 0 804 470" aria-label="We're at the Crest">
    <defs>
      <linearGradient id="letterFill" x1="0" y1="0" x2="0" y2="1">
        <stop offset="0" stop-color="var(--letter-light)"/>
        <stop offset="1" stop-color="var(--letter-dark)"/>
      </linearGradient>
    </defs>
    <text class="headline-kicker" x="120" y="118" font-size="92" textLength="564" lengthAdjust="spacingAndGlyphs">WE'RE AT THE</text>
    <text class="headline-word" x="78" y="462" font-size="330" fill="url(#letterFill)" textLength="648" lengthAdjust="spacingAndGlyphs">CREST</text>
  </svg>

  <h1 class="event-title">WELCOME WEEK 2013</h1>

  <div class="footer-ship" role="img" aria-label="Faint silhouette of a steamboat"></div>

  <div class="schedule">
    <div class="schedule-column">
      <div class="event"><p>Thursday August 22:</p><p>Residence Hall Move-In</p><p>12:00pm-3:00pm</p><p>Ridge Hall</p></div>
      <div class="event"><p>Brunch</p><p>10:00am-1:00pm</p><p>Dining Hall</p></div>
      <div class="event"><p>International Students Orientation</p><p>3:00pm</p><p>Hartley 121</p></div>
      <div class="event"><p>Dinner</p><p>5:00pm-6:30pm</p><p>Dining Hall</p><p>Hot Springs Waterslide Party</p><p>7:00pm-9:00pm</p><p>Valley Hot Springs</p></div>
      <div class="event"><p>Friday August 23:</p><p>Breakfast</p><p>7:30am-9:00am</p><p>Dining Hall</p></div>
      <div class="event"><p>Hike Aspen Creek Falls</p><p>9:00am-11:30am</p><p>Shuttle leaves Ridge Hall at 8:30am</p></div>
      <div class="event"><p>BBQ and Faculty Ice Cream Social</p><p>12:00pm-1:30pm</p><p>Dining Hall</p></div>
      <div class="event"><p>Kick Off Party: Inflatables</p><p>1:30pm-4:00pm</p><p>Upper Parking Lot</p></div>
      <div class="event"><p>Dinner</p><p>5:00pm-6:00pm</p><p>Dining Hall</p></div>
    </div>
    <div class="schedule-column">
      <div class="event"><p>Free Concert</p><p>7:00pm</p><p>Summit Resort Base</p><p>(PCT Buses to Resort,</p><p>5:35pm Last Bus)</p></div>
      <div class="event"><p>Saturday August 24:</p><p>Center Street Farmers Market</p><p>9:00am-2:00pm</p><p>6th&amp; Elm (walking dist.)</p></div>
      <div class="event"><p>Brunch</p><p>10:00am-1:00pm</p><p>Dining Hall</p></div>
      <div class="event"><p>Berry Meadow Hot Springs</p><p>2:00pm-5:00pm</p><p>Shuttle leaves Ridge Hall at 1:30pm</p></div>
      <div class="event"><p>Dinner</p><p>5:00-6:00pm</p><p>Dining Hall</p></div>
      <div class="event"><p>Free Movie on the Mountain: Star Quest</p><p>8:00pm</p><p>(PCT Buses to Resort,</p><p>5:35pm Last Bus)</p></div>
      <div class="event"><p>Sunday August 25:</p><p>Brunch</p><p>10:00am-1:00pm</p><p>Dining Hall</p></div>
      <div class="event"><p>Alpine Slide/Volleyball</p><p>2:00pm-4:00pm</p><p>Meet at Larkspur Hill</p></div>
      <div class="event"><p>Dinner</p><p>5:00pm-6:00pm</p><p>Dining Hall</p></div>
      <div class="event"><p>Mandatory All Hall Meeting</p><p>6:00pm</p><p>Auditorium</p></div>
    </div>
    <div class="schedule-column">
      <div class="event"><p>RHA Super Sunday Program</p><p>8:00pm</p><p>Ridge Hall: MPR</p></div>
      <div class="event"><p>Monday August 26:</p><p>Regular Dining Hall Hours Begin</p></div>
      <div class="event"><p>"Being Alone Sucks!"</p><p>9:00pm</p><p>Auditorium</p></div>
      <div class="event"><p>&nbsp;</p><p>Tuesday August 27:</p><p>Newly Roommate Game</p><p>7:00pm-8:00pm</p><p>Ridge Hall: MPR</p></div>
      <div class="event"><p>Free Gelato</p><p>8:00pm-9:00pm</p><p>Bella Gelato 7th and Birch</p></div>
      <div class="event"><p>Wednesday August 28:</p><p>Free Bowling</p><p>9:00pm</p><p>Frost Lanes</p></div>
      <div class="event"><p>Thursday August 29:</p><p>Club Fair</p><p>10:00am-2:00pm</p><p>Dining Hall</p></div>
      <div class="event"><p>Black Light Dodgeball</p><p>9:00pm</p><p>Gym</p></div>
      <div class="event"><p>Friday August 30:</p><p>Late Night Climbing</p><p>9:00pm</p><p>Gym</p></div>
      <div class="event"><p>ALL EVENTS ARE FREE</p><p>UNLESS OTHERWISE NOTED</p></div>
    </div>
  </div>

  <div class="brand">
    <span class="brand-dot"></span>
    <span class="brand-name">Granite Ridge College</span>
  </div>
</div>
</body>
</html>
```